Winter Carnival - FUN Web Design Project

The winter carnival is celebrating it's 50th anniversary this year and we are looking to have a new website that will not only work for the 50th, but will work for future years as well (so cannot be 100% geared to the anniversary in terms of look & feel).

The primary focus of the Carnival is the events that take place through the 10-day carnival, and giving recognition to the sponsors (rotating logos on splash page / interior).

The primary colours of the Carnival are Red and White. For some background information - see the old site parked here: http://www.frelkamp.on.ca/content.php?ID=34

For the design concepts, we welcome stock photography as we would like to see several photos located prominently throughout the site which we will provide once the site is being constructed (no need to buy stock - we have lots of photos that we can use once a design is selected).

The carnival is a WINTER carnival - so obviously a winter theme utilizing the Red / White colours of our brand.

PSD files will be required so we can code the site to our needs from a technical perspective.
Updates

Good quality GIF of logo attached with lower-quality (sorry) version of the Wordmark uploaded to Project File.

Date extended 1 day to Sunday!

Industry/Entity Type

Events

Requirements
Must have
• Prominent placement for key sponsor logos
Links to social media - ChatterPage / Quillow / Snapboard
Photo-friendly website
Incorporation of corporate colours - Red / White
1 x Home/Splash page layout - emphasis on sponsors, photos, featured event
1 x Interior page layout - more focused on content - see http://www.frelkamp.on.ca/content.php?ID=34
Site search bar
Drop-down navigation / changing colour rollovers
Child - Friendly

Nice to have
• Banner/Image links to other site features:
- news
- photo gallery
- History

```html
<!DOCTYPE html>
<html lang="en">
<head>
<meta charset="utf-8">
<title>Frelkamp Winter Carnival</title>
<link href="https://fonts.googleapis.com/css2?family=Ubuntu:wght@400;500;700&family=Kaushan+Script&display=swap" rel="stylesheet">
<style>
:root{
  --red:#d71f28;
  --red-dark:#a8121a;
  --ink:#2b2b2b;
  --nav:#2f2f2f;
  --sky:#3f86b4;
  --sky-light:#7fb6d6;
  --blue-head:#1a8cc4;
  --grey-text:#444;
  --footer:#2a2a2a;
  --white:#fff;
}
*{margin:0;padding:0;box-sizing:border-box}
html,body{width:1114px;height:1200px;overflow:hidden;background:var(--sky)}
.stage{position:absolute;left:0;top:0;width:1300px;height:1400px;transform:scale(.85692);transform-origin:0 0;font-family:Arial,Helvetica,sans-serif;color:var(--grey-text)}
.backdrop{position:absolute;inset:0;background:radial-gradient(ellipse at 50% 30%,var(--sky-light),var(--sky) 70%)}
.page{position:absolute;left:152px;top:0;width:996px;height:1200px;background:var(--white)}
.abs{position:absolute}
.topline{left:10px;top:0;width:976px;height:5px;background:var(--ink)}
.brand{left:24px;top:50px;display:flex;align-items:center;gap:12px;font-family:Ubuntu,sans-serif;font-weight:700;font-size:40px;color:var(--red)}
.brand i{display:block;width:46px;height:46px;border-radius:50%;background:var(--red)}
.phone{left:765px;top:5px;width:178px;height:37px;background:var(--ink);color:#fff;font-family:Ubuntu,sans-serif;font-size:17px;display:flex;align-items:center;justify-content:center;gap:8px}
.search{left:658px;top:76px;display:flex}
.search input{width:222px;height:28px;border:1px solid #e2e2e2;border-radius:4px 0 0 4px;padding-left:12px;font-family:Ubuntu,sans-serif;font-size:12px;color:#999;background:#fafafa}
.search button{width:74px;height:28px;border:0;border-radius:0 4px 4px 0;background:var(--red);color:#fff;font-family:Ubuntu,sans-serif;font-size:13px}
.nav{left:10px;top:141px;width:976px;height:43px;background:var(--nav);display:flex;list-style:none}
.nav li{color:#fff;font-family:Ubuntu,sans-serif;font-size:12px;display:flex;align-items:center;justify-content:center;border-right:1px solid #555}
.nav li.active{background:var(--red);border-bottom:2px dashed #fff}
.hero{left:10px;top:186px;width:976px;height:369px;background:linear-gradient(100deg,#c8b9b3 0%,#e9e1dc 30%,#dcc2bf 50%,#bfa79c 72%,#8f7f76 100%)}
.hero-card{left:38px;top:49px;width:600px;height:213px;border:2px solid #fff;border-radius:16px;background:rgba(255,255,255,.72);padding:12px 8px}
.hero-card h1{font-family:Ubuntu,sans-serif;font-size:44px;color:var(--ink);line-height:1.05;font-weight:700}
.script{font-family:'Kaushan Script',cursive;color:var(--red);font-weight:400}
.hero-card h1 .small{font-family:'Kaushan Script',cursive;color:var(--ink);font-size:40px;font-weight:400}
.hero-card p{font-family:Ubuntu,sans-serif;font-size:15px;line-height:22px;color:#333;margin-top:14px;padding:0 4px;text-align:justify}
.sponsor-strip{left:10px;top:560px;width:971px;height:90px;background:linear-gradient(#fff,#e9e9e9);display:flex;align-items:center;justify-content:space-around;padding:0 30px}
.badge{height:60px;border-radius:6px}
.main-title{left:41px;top:672px;font-family:Ubuntu,sans-serif;font-weight:500;font-size:22px;color:var(--ink)}
.main-title .script{font-size:26px}
.rule{left:40px;top:706px;width:628px;border-top:1px dashed #aaa}
.rule-end{left:667px;top:696px;height:24px;border-left:1px solid #aaa}
.copy{left:30px;width:635px;font-size:11.5px;line-height:18px;letter-spacing:.4px;text-align:justify}
.copy b{color:var(--ink)}
.section-title{left:20px;top:912px;font-family:Ubuntu,sans-serif;font-weight:700;font-size:20px;color:var(--blue-head)}
.card{width:206px}
.card .photo{height:122px;border:3px solid #eee;box-shadow:0 0 2px #bbb}
.card p{font-size:11px;line-height:14.5px;letter-spacing:.4px;text-align:justify;margin-top:8px;padding:0 2px}
.card p b{color:#111}
.more{display:block;width:76px;margin:6px 4px 0 auto;background:#555;color:#fff;font-family:Ubuntu,sans-serif;font-size:11px;text-align:center;border-radius:2px;padding:1px 0}
.divider{left:692px;top:690px;height:440px;width:8px;background:linear-gradient(90deg,rgba(0,0,0,.06),transparent)}
.news{left:729px;top:670px;width:252px;height:274px;border:1px solid #ddd;border-radius:6px;background:linear-gradient(#fff,#f4f4f4)}
.tab{left:723px;top:690px;width:228px;height:32px;background:linear-gradient(var(--red),var(--red-dark));border-radius:3px 10px 10px 3px;color:#fff;font-family:Ubuntu,sans-serif;font-weight:700;font-size:18px;padding:5px 25px}
.news-item{left:743px;display:flex;gap:8px;width:232px}
.news-item .thumb{width:44px;height:36px;background:linear-gradient(#e6e6e6,#c4c4c4);border:2px solid #fff;box-shadow:0 0 2px #999;flex:none}
.news-item div p{font-size:11.5px;line-height:18px;letter-spacing:.4px;color:#333}
.news-item div p b{color:#222}
.news-item .meta{font-size:11px;color:#555}
.view-more{left:896px;top:920px;font-size:12px;color:#222}
.sponsor-bar{left:720px;top:972px;width:222px;height:29px;background:#555;clip-path:polygon(0 0,92% 0,100% 50%,92% 100%,0 100%);color:#fff;font-family:Ubuntu,sans-serif;font-weight:700;font-size:18px;padding:3px 13px}
.sponsor-mark{left:740px;top:1030px;width:205px;height:110px;display:flex;align-items:center;justify-content:center;gap:10px;font-family:Ubuntu,sans-serif;font-size:18px;color:#3f7f3f}
.sponsor-mark i{display:block;width:40px;height:40px;border-radius:50%;background:#7ab060}
.footer{position:absolute;left:140px;top:1200px;width:1020px;height:200px;background:linear-gradient(#333,var(--footer));border-top:10px solid var(--red)}
.footer h3{font-family:Ubuntu,sans-serif;font-weight:400;font-size:20px;color:#fff;margin-bottom:10px}
.footer .col{position:absolute;top:8px;color:#eee;font-size:12px;line-height:18px;letter-spacing:.6px}
.footer ul{list-style:none}
.social li{display:flex;align-items:center;gap:10px;height:30px}
.social i{display:block;width:18px;height:18px;background:#777;border-radius:2px}
.footer-brand{position:absolute;left:878px;top:40px;width:124px;font-family:Ubuntu,sans-serif;font-weight:700;font-size:22px;color:#fff;display:flex;flex-direction:column;align-items:center;gap:10px}
.footer-brand i{display:block;width:50px;height:50px;border-radius:50%;background:var(--red)}
</style>
</head>
<body>
<div class="stage">
  <div class="backdrop" role="img" aria-label="Blue winter background with ribbon-wrapped tree decorations and snowflakes"></div>

  <div class="page">
    <div class="abs topline"></div>
    <div class="abs brand"><i></i>Frelkamp</div>
    <div class="abs phone">
      <svg width="20" height="18" viewBox="0 0 20 18"><rect x="1" y="2" width="10" height="14" rx="2" fill="none" stroke="#e33" stroke-width="2"/><path d="M14 5q3 4 0 8M16.5 3q5 6 0 12" fill="none" stroke="#e33" stroke-width="1.6"/></svg>
      (705) 555-0142
    </div>
    <form class="abs search"><input type="text" value="i'am searching for…" aria-label="Search"><button type="button">Search</button></form>

    <ul class="abs nav">
      <li style="width:75px">Home</li>
      <li class="active" style="width:112px">Opening Night</li>
      <li style="width:72px">Events</li>
      <li style="width:121px">Premier Concert</li>
      <li style="width:80px">Kid Zone</li>
      <li style="width:110px">Photo Gallery</li>
      <li style="width:122px">Polor Bear Swim</li>
      <li style="width:87px">Sponsors</li>
      <li style="width:100px">Carnival Info</li>
      <li style="width:97px;border:0">Contact Us</li>
    </ul>

    <div class="abs hero" role="img" aria-label="Carnival photo collage: red sports car, costumed snowman mascot and a decorated circus elephant">
      <div class="abs hero-card">
        <h1>The Largest <span class="script">Winter</span><br><span class="script">Carnival</span> <span class="small">in northern Ontario</span></h1>
        <p>The point of using Lorem Ipsum is that it has a more-or-less normal distribution of letters, as opposed to using 'Content here, content here', making it look like readable English. Many desktop publishing packages and web page editors now use</p>
      </div>
    </div>

    <div class="abs sponsor-strip">
      <div class="badge" style="width:170px;background:#dbe9f1"></div>
      <div class="badge" style="width:107px;background:#a9cc66"></div>
      <div class="badge" style="width:125px;background:#e2ecdb"></div>
      <div class="badge" style="width:110px;background:#cfe2f3"></div>
      <div class="badge" style="width:125px;background:#e4e4e4"></div>
      <div class="badge" style="width:120px;background:#e3efd3"></div>
      <div class="badge" style="width:60px;background:#f4d3d3;border-radius:50%"></div>
    </div>

    <h2 class="abs main-title">His winning entry was, of course <span class="script">"Frelkamp"</span></h2>
    <div class="abs rule"></div><div class="abs rule-end"></div>

    <p class="abs copy" style="top:722px">Frelkamp - as we now know it - was originally the idea of Harrow Falls businessman Walter Penrose. The first Carnival was held in 1964. In the beginning it was a collection of events that already existed in the City, but were encouraged by the Chamber of Commerce to come together in a Carnival Format. Frelkamp - as we now know it - was originally the idea of Harrow Falls businessman Walter Penrose.</p>
    <p class="abs copy" style="top:812px"><b>The first Carnival was held in 1964</b>. In the beginning it was a collection of events that already existed in the City, but were encouraged by the Chamber of Commerce to come together in a Carnival Format. The primary purpose was to add excitement to the long winter season - but early organizers also recognized this great opportunity to boost Tourism and business during the historically slower first quarter of the year.</p>

    <h2 class="abs section-title">Polar Bear Swim</h2>
    <div class="abs card" style="left:19px;top:945px">
      <div class="photo" role="img" aria-label="Mascot posing with a group of swimmers in team jerseys" style="background:linear-gradient(#c9d0c4,#9fa99b 60%,#c99a98)"></div>
      <p><b>In the beginning</b> it was a collection of events that already existed in the City, but were encouraged by the Chamber of Commerce</p>
      <span class="more">more Info [+]</span>
    </div>
    <div class="abs card" style="left:242px;top:942px">
      <div class="photo" role="img" aria-label="Mascot waving on stage at night" style="background:linear-gradient(#6a6262,#a88886 60%,#d8b2b0)"></div>
      <p><b>In the beginning</b> it was a collection of events that already existed in the City, but were encouraged by the Chamber of Commerce</p>
      <span class="more">more Info [+]</span>
    </div>
    <div class="abs card" style="left:468px;top:942px">
      <div class="photo" role="img" aria-label="Mascot among snow sculptures and visitors" style="background:linear-gradient(#e6ebef,#f4f4f4 55%,#e2c4c4)"></div>
      <p><b>In the beginning</b> it was a collection of events that already existed in the City, but were encouraged by the Chamber of Commerce</p>
      <span class="more">more Info [+]</span>
    </div>

    <div class="abs divider"></div>

    <div class="abs news"></div>
    <div class="abs tab">Latest News</div>
    <div class="abs news-item" style="top:738px"><span class="thumb"></span><div><p><b>Lorem Ipsum is simply text of the</b> printing</p><p class="meta">May 15, 2012 // 4 Comments</p></div></div>
    <div class="abs news-item" style="top:797px"><span class="thumb"></span><div><p><b>Lorem Ipsum is simply text of the</b> printing</p><p class="meta">May 15, 2012 // 4 Comments</p></div></div>
    <div class="abs news-item" style="top:857px"><span class="thumb"></span><div><p><b>Lorem Ipsum is simply text of the</b> printing</p><p class="meta">May 15, 2012 // 4 Comments</p></div></div>
    <span class="abs view-more">View more [+]</span>

    <div class="abs sponsor-bar">Our Sponsors</div>
    <div class="abs sponsor-mark"><i></i>Harrow Falls</div>
  </div>

  <footer class="footer">
    <div class="col" style="left:67px">
      <h3>Navigate</h3>
      <ul><li>Home</li><li>Northbank Opening</li><li>Ceremonies</li><li>Events</li><li>Kid Zone</li><li>Photo Gallery</li><li>Contact Us</li></ul>
    </div>
    <div class="col" style="left:249px;width:220px;text-align:justify">
      <h3>Our History</h3>
      <p>Frelkamp - as we now know it - was originally the idea of Harrow Falls businessman Walter Penrose. The first Carnival was held in 1964. In the beginning it was a collection of events that already existed in the City.</p>
    </div>
    <div class="col" style="left:547px">
      <h3>Contact us</h3>
      <p>88 - B Ashgrove Street<br>Harrow Falls, Ontario<br>P0X 1A0<br>Tel: (705) 555-0142<br>Fax: (705) 555-0187</p>
    </div>
    <div class="col" style="left:756px">
      <h3>Media Links</h3>
      <ul class="social"><li><i></i>ChatterPage</li><li><i></i>Quillow</li><li><i></i>Snapboard</li><li><i></i>Circlenet</li></ul>
    </div>
    <div class="footer-brand"><i></i>Frelkamp</div>
  </footer>
</div>
</body>
</html>
```